Velmora Trade Hall (front page)

We need a design of a front page for our Velmora Trade Hall website (vth.co.uk). Our company is based in the United Kingdom and offers investors from all over the world an opportunity to invest into bitcoin and litecoin.

We have been developing this cutting edge technology for past 2 years based on our in depth knowledge on conventional stock and currency trading technology and methodology. We have run many test against penetration, security and stability and now are ready to deploy.

Recent news about vulnerability of such platforms leave a great deal of unease from retail investors about investing into cryptocurrency. We are set to challenge this attitude. Our background is payments in particular regulated environment in the UK. We are keen to apply our wealth of experience to provide secure and reliable trading platform and advance cryptocurrency as means of legal tender.

The front page should be based on the feel and look of our current technology vth.co.uk. Some of you have already been involved in logo design for our company, please see the attached mockups. The page should have this minimalist design, very clean and light.

Seek inspiration form www.korvelin.net, www.trusmarq.com, vip.plomwerth.com and other bitcoin exchanges.

We look forward to receiving your ideas.

You can also refer to our social pages:
https://www.facebook.com/vth.co.uk
https://twitter.com/vth_uk

We would like you to focus your efforts at designing the page in such a way so that it is very easy for visitor be open an account with the exchange. We must focus at informing the visitor about the bitcoin, how to my buy, how to sell, look at the general overview of the maker and CONVERTING him/her sing up. This is the most important!!

Regards,
Oren

Reason: Dear all, We are very keen on getting this design done right the first time. The key success is conversion of visitors to subscribers and then to traders. It is absolutely essential make the registration process as streamlined as possible! When we are calling them to act by "Change the world one bitcoin at a time" we should give them a opportunity to provide us with relevant account creation details: email, password, confirm password. Please visit quenzo.co.uk for ideas. Secondly, tell them what is a bitcoin, why a bitcoin is a good investment and how to invest. Finally, it is important to inform visitors of "who we are", what sets us apart from other exchanges, tell them about our experience. In our view graphs and live order books are important but they might turn some visitors away especially the ones that are not accustomed to online trading. Think of what would you like to see on the page if you wanted YOURSELF to invest. What would make you to create an account and use it? Think what will work, we are here to revolutionise how people do business.... any wild ideas put them to us. OUR BUDGET JUST GONE UP!!!

Target Market(s)

A combination of professional and consumer bitcoin investors.

Requirements
Must have
• News section

```html
<!DOCTYPE html>
<html lang="en">
<head>
<meta charset="utf-8">
<title>Velmora Trade Hall</title>
<link rel="stylesheet" href="https://fonts.googleapis.com/css2?family=Open+Sans:wght@400;600;700&family=Roboto+Slab:wght@400;700&display=swap">
<style>
:root{
  --blue:#1aa5dc;
  --blue-dark:#0d8cc3;
  --blue-mid:#55c2ea;
  --blue-light:#8dd5ef;
  --yellow:#f9c10e;
  --orange:#f3a93a;
  --ink:#333333;
  --ink-soft:#666666;
  --grey-text:#8a8a8a;
  --line:#dddddd;
  --paper:#ffffff;
  --well:#eeeeee;
  --footer:#353535;
  --red:#e2403a;
  --sans:'Open Sans', Arial, sans-serif;
  --slab:'Roboto Slab', Georgia, serif;
}
*{box-sizing:border-box;margin:0;padding:0}
html,body{width:685px;height:1200px;overflow:hidden;background:var(--paper)}
body{font-family:var(--sans);color:var(--ink)}
.page{position:relative;width:685px;height:1200px;overflow:hidden;background:var(--paper)}
.abs{position:absolute}

/* ticker bar */
.ticker{left:0;top:0;width:685px;height:23px;background:#3a3a3a;color:#d8d8d8;font-size:7px}
.ticker span{position:absolute;top:7px}
.ticker b{font-weight:400;color:#fff}
.ticker .volume{color:var(--blue-mid)}

/* header */
.masthead{left:0;top:23px;width:685px;height:57px;background:linear-gradient(#f3f3f3,#ffffff)}
.brand{left:99px;top:15px;display:flex;align-items:center;gap:8px}
.brand-dot{width:16px;height:16px;border-radius:50%;background:var(--blue)}
.brand-name{font-size:9px;letter-spacing:3px;color:var(--ink);font-weight:400}
.hotline{left:518px;top:21px;display:flex;align-items:center;gap:5px;font-size:10px;color:var(--ink)}

/* nav */
.nav{left:0;top:80px;width:685px;height:28px;background:#fff;border-top:1px solid #e6e6e6}
.nav ul{list-style:none;position:absolute;left:98px;top:0;display:flex;height:28px}
.nav li{font-size:7px;display:flex;align-items:center;justify-content:center;height:28px;position:relative;color:var(--ink)}
.nav li+li::before{content:"";position:absolute;left:0;top:11px;height:8px;border-left:1px solid #bbb}
.nav li.current{background:var(--blue);color:#fff}
.nav li.current+li::before{display:none}

/* hero */
.hero{left:0;top:108px;width:685px;height:223px;background:linear-gradient(180deg,#22b0e4,#139dd6);overflow:hidden}
.hero-grid{left:0;top:0;width:685px;height:223px;background-image:linear-gradient(rgba(255,255,255,.06) 1px,transparent 1px),linear-gradient(90deg,rgba(255,255,255,.06) 1px,transparent 1px);background-size:58px 58px}
.hero-kicker{left:0;width:685px;top:36px;text-align:center;font-size:11px;letter-spacing:2px;color:#fff;font-weight:400}
.hero-kicker span{margin-left:-20px}
.hero-title{left:98px;top:53px;font-size:20px;line-height:22px;font-weight:700;color:#fff}
.hero-copy{left:100px;top:100px;width:288px;font-size:6.5px;line-height:9px;color:#e6f6fd}
.hero-cta{left:98px;top:136px;width:122px;height:23px;background:var(--yellow);font-size:9px;font-weight:700;color:var(--ink);display:flex;align-items:center;justify-content:center}
.hero-art{left:392px;top:50px;width:293px;height:173px;background:radial-gradient(ellipse at 30% 30%,rgba(255,216,90,.55),rgba(255,255,255,.12) 40%,rgba(255,255,255,.04) 70%)}
.stat{top:180px;height:24px;color:#fff;font-weight:700;display:flex;align-items:center}
.stat-one{left:0;width:163px;background:var(--blue-dark);font-size:18px;padding-left:48px}
.stat-two{left:165px;width:106px;background:var(--blue-mid);font-size:14px;justify-content:center}
.stat-three{left:271px;width:88px;background:var(--blue-light);font-size:14px;justify-content:center}
.slider-dots{left:326px;top:203px;display:flex;gap:1px}
.slider-dots i{width:7px;height:7px;border-radius:50%;background:#e8e8e8;display:block}
.slider-dots i.on{background:#2b5f7a}

/* features */
.shade{left:40px;width:605px;height:10px;background:radial-gradient(ellipse at 50% 0,rgba(0,0,0,.18),transparent 70%)}
.feature{top:349px;width:168px;text-align:center}
.feature-badge{width:56px;height:56px;border-radius:50%;margin:0 auto;display:flex;align-items:center;justify-content:center}
.feature h2{font-family:var(--slab);font-weight:700;font-size:15px;margin-top:13px;color:var(--ink)}
.feature p{font-size:6.5px;line-height:9px;color:var(--ink-soft);width:150px;margin:16px auto 0}
.feature-rule{top:352px;width:1px;height:138px;background:linear-gradient(transparent,#e2e2e2,transparent)}

/* chart */
.chart{left:103px;top:520px;width:480px;height:189px;background:#fff;box-shadow:0 1px 4px rgba(0,0,0,.3)}

/* orders */
.well{left:0;top:760px;width:685px;height:268px;background:var(--well)}
.order-tab{top:735px;height:26px;width:102px;font-size:7px;font-weight:600;display:flex;align-items:center;justify-content:center}
.order-tab.dark{background:linear-gradient(#2a9fd2,#1379ab);color:#fff}
.order-tab.light{background:#fff;color:var(--ink);border:1px solid #ddd;border-bottom:none;font-weight:400}
.orders{left:99px;top:775px;width:320px;border-collapse:collapse;font-size:6.5px;background:#fff}
.orders th{color:var(--blue);font-weight:600;height:16px;text-align:left}
.orders td{height:18.4px;border-top:1px solid #e4e4e4;color:var(--ink)}
.orders tr:nth-child(even) td{background:#f4f4f4}
.orders th,.orders td{padding-left:0}
.c-market{width:46px;padding-left:6px!important}
.c-time{width:78px}
.c-type{width:32px}
.c-vol{width:55px;text-align:center!important}
.c-price{width:55px;text-align:center!important}
.c-total{width:48px;text-align:center!important}
.scroll-track{left:412px;top:785px;width:6px;height:215px;background:var(--blue)}
.scroll-thumb{left:413px;top:787px;width:4px;height:40px;background:#9fd8ef}

/* trade ticket */
.ticket{left:440px;top:737px;width:118px;height:128px;background:#fff;box-shadow:0 1px 3px rgba(0,0,0,.3)}
.ticket-head{display:flex;height:22px}
.ticket-head div{flex:1;color:#fff;text-align:center;font-size:6.5px;font-weight:700;line-height:8px;padding-top:3px}
.ticket-head small{display:block;font-weight:400;font-size:5.5px}
.ticket-buy{background:var(--blue)}
.ticket-sell{background:var(--orange)}
.ticket-row{position:absolute;left:8px;font-size:5.5px;color:var(--ink)}
.ticket-field{position:absolute;left:55px;width:56px;height:9px;border:1px solid #ccc;background:#fff;font-size:5.5px;padding-left:2px;line-height:7px}
.ticket-btn{position:absolute;top:84px;width:48px;height:15px;font-size:6.5px;color:#fff;display:flex;align-items:center;justify-content:center}
.ticket-note{position:absolute;left:0;width:118px;top:103px;font-size:4.5px;color:#999;text-align:center}

/* market list */
.markets{left:444px;top:877px;width:135px;height:122px;background:#fff;box-shadow:0 1px 3px rgba(0,0,0,.3)}
.markets-tabs{display:flex;height:14px;font-size:6px;border-bottom:1px solid #ddd}
.markets-tabs div{flex:1;display:flex;align-items:center;justify-content:center}
.markets-tabs .fav{background:#f1f1f1;color:#888}
.market-row{height:17px;display:flex;align-items:center;font-size:6.5px;border-bottom:1px solid #eee;position:relative}
.market-row.hot{background:#fdf7dc}
.market-row .star{width:14px;text-align:center;color:#ccc;font-size:6px}
.market-row .pair{width:36px}
.market-row svg{width:30px;height:10px}
.market-row .val{width:42px;text-align:right;color:var(--red)}
.market-row .val.up{color:var(--blue)}
.market-row .dir{width:10px;text-align:center;font-size:5px;color:var(--red)}
.market-row .dir.up{color:var(--blue)}

/* footer */
.footer{left:0;top:1028px;width:685px;height:172px;background:var(--footer);color:#ddd}
.footer h3{font-family:var(--slab);font-weight:400;font-size:10.5px;color:#fff;display:flex;align-items:center;gap:7px}
.news-item{font-size:6.2px;line-height:8px;margin-top:8px;width:148px;padding-bottom:6px;border-bottom:1px solid #555}
.news-date{font-family:var(--slab);font-weight:700;color:#4fb8e4;font-size:6.5px}
.news-title{color:#fff}
.news-body{color:#aaa}
.contact-line{display:flex;align-items:flex-start;gap:10px;font-size:6px;line-height:8px;color:#fff;margin-top:9px}
.social{display:flex;gap:6px;margin-top:10px}
.social span{width:12px;height:12px;background:#fff;border-radius:2px;display:block}
.subscribe-copy{font-size:6.3px;line-height:8.5px;color:#fff;width:145px;margin-top:10px}
.subscribe-input{width:140px;height:17px;background:#fff;font-size:5.5px;color:#bbb;padding-left:6px;line-height:17px;margin-top:6px}
.subscribe-btn{left:549px;top:73px;width:38px;height:19px;background:var(--yellow);font-size:7px;font-weight:700;color:var(--ink);display:flex;align-items:center;justify-content:center}
.view-all{left:221px;top:148px;font-size:6.5px;color:#fff;border-bottom:1px solid #fff}
</style>
</head>
<body>
<div class="page">

  <div class="abs ticker">
    <span style="left:98px">Last price | <b>563.798 USD</b></span>
    <span style="left:192px">Low price | <b>556.33 USD</b></span>
    <span style="left:285px">High price | <b>576.05 USD</b></span>
    <span class="volume" style="left:393px">Volume | 438.0 BTC</span>
    <span style="left:534px">Login | Register</span>
  </div>

  <header class="abs masthead">
    <div class="abs brand">
      <span class="brand-dot"></span>
      <span class="brand-name">VELMORA TRADE HALL</span>
    </div>
    <div class="abs hotline">
      <svg width="11" height="11" viewBox="0 0 12 12"><circle cx="6" cy="6" r="5.3" fill="none" stroke="#1aa5dc" stroke-width="1.3"/><path d="M4 3.3c.5-.3.9 0 1.1.5l.3.7c.1.3 0 .5-.2.7l-.3.3c.3.7.8 1.2 1.5 1.5l.3-.3c.2-.2.4-.3.7-.2l.7.3c.5.2.7.6.4 1.1-.4.6-1 .8-1.8.5-1.6-.6-2.7-1.7-3.3-3.3-.3-.8 0-1.4.6-1.8z" fill="#1aa5dc"/></svg>
      <span>245 56 56 56</span>
    </div>
  </header>

  <nav class="abs nav">
    <ul>
      <li class="current" style="width:52px">Home</li>
      <li style="width:70px">Account</li>
      <li style="width:70px">Buy / Sell</li>
      <li style="width:72px">Order Book</li>
      <li style="width:74px">Deposit</li>
      <li style="width:76px">Withdrawal</li>
      <li style="width:80px">Contact Us</li>
    </ul>
  </nav>

  <section class="abs hero">
    <div class="abs hero-grid"></div>
    <div class="abs hero-art" role="img" aria-label="Illustration: a gold coin and a silver coin joined by a hand, above line icons of a clock and a globe"></div>
    <div class="abs hero-kicker"><span>Sell BTC 604.29200 USD</span></div>
    <h1 class="abs hero-title">Trade at Multiple Exchanges<br>Using One Increadible Platform</h1>
    <p class="abs hero-copy">Suspendisse commodo interdum est in facilisis. Proin id mi feugiat, venenatis nisl nec, elementum tellus. Praesent id turpis et odio commodo dignissim. Integer id orci tortor.</p>
    <div class="abs hero-cta">Click here to view more</div>
    <div class="abs stat stat-one">230 000</div>
    <div class="abs stat stat-two">90 000</div>
    <div class="abs stat stat-three">82 000</div>
    <div class="abs slider-dots"><i class="on"></i><i></i><i></i></div>
  </section>
  <div class="abs shade" style="top:331px"></div>

  <div class="abs feature-rule" style="left:259px"></div>
  <div class="abs feature-rule" style="left:427px"></div>

  <section class="abs feature" style="left:90px">
    <div class="feature-badge" style="background:var(--blue)">
      <svg width="22" height="24" viewBox="0 0 22 24"><path d="M6 11V7a5 5 0 0 1 10 0v4" fill="none" stroke="#fff" stroke-width="2.6"/><rect x="3" y="10" width="16" height="13" rx="2" fill="#fff"/></svg>
    </div>
    <h2>Security</h2>
    <p>Aenean et lectus cursus, aliquam ipsum cursus, ornare eros. Donec varius purus vel sem pharetra convallis nec eu nisi. Sed id felis elementum, dapibus odio id, malesuada mi.</p>
  </section>

  <section class="abs feature" style="left:258px">
    <div class="feature-badge" style="background:var(--yellow)">
      <svg width="26" height="26" viewBox="0 0 26 26"><g fill="none" stroke="#fff" stroke-width="3" stroke-linecap="round"><path d="M11 8l3-3a4 4 0 0 1 6 6l-3 3"/><path d="M15 18l-3 3a4 4 0 0 1-6-6l3-3"/></g><g stroke="#fff" stroke-width="1.4"><path d="M12 12l-3-3M14 14l3 3M13 11V8M11 13H8"/></g></svg>
    </div>
    <h2>How it Works</h2>
    <p>Aenean et lectus cursus, aliquam ipsum cursus, ornare eros. Donec varius purus vel sem pharetra convallis nec eu nisi. Sed id felis elementum, dapibus odio id, malesuada mi.</p>
  </section>

  <section class="abs feature" style="left:426px">
    <div class="feature-badge" style="background:var(--ink)">
      <svg width="24" height="20" viewBox="0 0 24 20" fill="#fff"><rect x="0" y="0" width="6" height="5" rx="1"/><rect x="8" y="0" width="16" height="5" rx="1"/><rect x="0" y="7.5" width="6" height="5" rx="1"/><rect x="8" y="7.5" width="16" height="5" rx="1"/><rect x="0" y="15" width="6" height="5" rx="1"/><rect x="8" y="15" width="16" height="5" rx="1"/></svg>
    </div>
    <h2>Features</h2>
    <p>Aenean et lectus cursus, aliquam ipsum cursus, ornare eros. Donec varius purus vel sem pharetra convallis nec eu nisi. Sed id felis elementum, dapibus odio id, malesuada mi.</p>
  </section>
  <div class="abs shade" style="top:500px"></div>

  <section class="abs chart">
    <svg width="480" height="189" viewBox="101 510 471 185" preserveAspectRatio="none" font-family="Open Sans, Arial, sans-serif">
      <defs>
        <linearGradient id="areaFill" x1="0" y1="0" x2="0" y2="1">
          <stop offset="0" stop-color="#cfe8f7"/>
          <stop offset="1" stop-color="#f2f9fd"/>
        </linearGradient>
      </defs>
      <g font-size="5.5" fill="#333">
        <rect x="107" y="515" width="10" height="9" fill="#fbf3c7" stroke="#ccc" stroke-width=".5"/><text x="109" y="521.5">M1</text>
        <rect x="118" y="515" width="12" height="9" fill="#fff" stroke="#ccc" stroke-width=".5"/><text x="120" y="521.5">M5</text>
        <rect x="131" y="515" width="15" height="9" fill="#fff" stroke="#ccc" stroke-width=".5"/><text x="132.5" y="521.5">M15</text>
        <rect x="147" y="515" width="15" height="9" fill="#fff" stroke="#ccc" stroke-width=".5"/><text x="148.5" y="521.5">M30</text>
        <rect x="163" y="515" width="10" height="9" fill="#fff" stroke="#ccc" stroke-width=".5"/><text x="164.5" y="521.5">H1</text>
        <rect x="174" y="515" width="10" height="9" fill="#fff" stroke="#ccc" stroke-width=".5"/><text x="175.5" y="521.5">H4</text>
      </g>
      <text x="336" y="522" font-size="7" font-weight="600" fill="#333" text-anchor="middle">BTC/USD</text>
      <g stroke="#e6e6e6" stroke-width=".5">
        <line x1="124" y1="561" x2="566" y2="561"/>
        <line x1="124" y1="590" x2="566" y2="590"/>
        <line x1="124" y1="620" x2="566" y2="620"/>
      </g>
      <g font-size="6" fill="#444">
        <text x="106" y="563">579</text>
        <text x="106" y="592">576.800</text>
        <text x="106" y="622">574.5</text>
        <text x="194" y="660">12:55</text>
        <text x="268" y="660">13:05</text>
        <text x="340" y="660">13:15</text>
        <text x="413" y="660">13:25</text>
        <text x="485" y="660">13:35</text>
      </g>
      <path d="M130 567L135 576L196 576L217 603L232 563L290 563L312 590L335 590L350 567L370 565L390 590L415 590L430 614L450 617L505 617L520 607L535 616L550 630L566 642L566 650L130 650Z" fill="url(#areaFill)"/>
      <polyline points="130,567 135,576 196,576 217,603 232,563 290,563 312,590 335,590 350,567 370,565 390,590 415,590 430,614 450,617 505,617 520,607 535,616 550,630 566,642" fill="none" stroke="#8cc4e6" stroke-width="1"/>
      <line x1="124" y1="650" x2="566" y2="650" stroke="#aaa" stroke-width=".5"/>
      <g stroke="#ccc" stroke-width=".5" fill="#fff">
        <rect x="101" y="679" width="118" height="16" stroke="none"/>
        <rect x="219" y="680" width="117" height="15" fill="#fafafa"/>
        <rect x="336" y="680" width="118" height="15" fill="#fafafa"/>
        <rect x="454" y="680" width="118" height="15" fill="#fafafa"/>
      </g>
      <g font-size="6" text-anchor="middle">
        <text x="160" y="689" fill="#333">QUOTES</text>
        <text x="277" y="689" fill="#999">CANDLES</text>
        <text x="395" y="689" fill="#999">DEPTH</text>
        <text x="513" y="689" fill="#999">VOLUME</text>
      </g>
    </svg>
  </section>

  <div class="abs well"></div>
  <div class="abs order-tab dark" style="left:99px">Active Order</div>
  <div class="abs order-tab light" style="left:207px">All Order</div>
  <div class="abs order-tab dark" style="left:314px">Trade History</div>

  <table class="abs orders">
    <thead>
      <tr><th class="c-market">Market</th><th class="c-time">Time</th><th class="c-type">Type</th><th class="c-vol">Volume (BTC)</th><th class="c-price">Price</th><th class="c-total">Total (USD)</th></tr>
    </thead>
    <tbody>
      <tr><td class="c-market">BTC/USD</td><td>3/24/2014 7:22:04 PM</td><td>Sell</td><td class="c-vol">0.00756</td><td class="c-price">565.58</td><td class="c-total">4.2758</td></tr>
      <tr><td class="c-market">BTC/USD</td><td>3/24/2014 7:22:04 PM</td><td>Sell</td><td class="c-vol">0.00756</td><td class="c-price">565.58</td><td class="c-total">4.2758</td></tr>
      <tr><td class="c-market">BTC/USD</td><td>3/24/2014 7:22:04 PM</td><td>Sell</td><td class="c-vol">0.00756</td><td class="c-price">565.58</td><td class="c-total">4.2758</td></tr>
      <tr><td class="c-market">BTC/USD</td><td>3/24/2014 7:22:04 PM</td><td>Sell</td><td class="c-vol">0.00756</td><td class="c-price">565.58</td><td class="c-total">4.2758</td></tr>
      <tr><td class="c-market">BTC/USD</td><td>3/24/2014 7:22:04 PM</td><td>Sell</td><td class="c-vol">0.00756</td><td class="c-price">565.58</td><td class="c-total">4.2758</td></tr>
      <tr><td class="c-market">BTC/USD</td><td>3/24/2014 7:22:04 PM</td><td>Sell</td><td class="c-vol">0.00756</td><td class="c-price">565.58</td><td class="c-total">4.2758</td></tr>
      <tr><td class="c-market">BTC/USD</td><td>3/24/2014 7:22:04 PM</td><td>Sell</td><td class="c-vol">0.00756</td><td class="c-price">565.58</td><td class="c-total">4.2758</td></tr>
      <tr><td class="c-market">BTC/USD</td><td>3/24/2014 7:22:04 PM</td><td>Sell</td><td class="c-vol">0.00756</td><td class="c-price">565.58</td><td class="c-total">4.2758</td></tr>
      <tr><td class="c-market">BTC/USD</td><td>3/24/2014 7:22:04 PM</td><td>Sell</td><td class="c-vol">0.00756</td><td class="c-price">565.58</td><td class="c-total">4.2758</td></tr>
      <tr><td class="c-market">BTC/USD</td><td>3/24/2014 7:22:04 PM</td><td>Sell</td><td class="c-vol">0.00756</td><td class="c-price">565.58</td><td class="c-total">4.2758</td></tr>
      <tr><td class="c-market">BTC/USD</td><td>3/24/2014 7:22:04 PM</td><td>Sell</td><td class="c-vol">0.00756</td><td class="c-price">565.58</td><td class="c-total">4.2758</td></tr>
    </tbody>
  </table>
  <div class="abs scroll-track"></div>
  <div class="abs scroll-thumb"></div>

  <aside class="abs ticket">
    <div class="ticket-head">
      <div class="ticket-buy">Buy BTC<small>578.78100 USD</small></div>
      <div class="ticket-sell">Sell BTC<small>577.0000 USD</small></div>
    </div>
    <span class="ticket-row" style="top:30px">Type</span>
    <div class="ticket-field" style="top:29px">Limit<span style="position:absolute;right:0;top:0;width:8px;height:7px;border-left:1px solid #ccc;font-size:4px;text-align:center">▼</span></div>
    <span class="ticket-row" style="top:42px">Volume BTC</span>
    <div class="ticket-field" style="top:41px"></div>
    <span class="ticket-row" style="top:54px">Price per BTC</span>
    <div class="ticket-field" style="top:53px"></div>
    <span class="ticket-row" style="top:68px">Total</span>
    <span class="ticket-row" style="top:68px;left:55px">Fee</span>
    <span class="ticket-row" style="top:76px">USD 0.0000</span>
    <span class="ticket-row" style="top:76px;left:55px">BTC 0.00000</span>
    <div class="ticket-btn" style="left:8px;background:var(--blue)">Buy BTC</div>
    <div class="ticket-btn" style="left:62px;background:#cfcfcf">Cancel</div>
    <div class="ticket-note">Commission for the transaction is 0.2%</div>
  </aside>

  <aside class="abs markets">
    <div class="markets-tabs"><div>ALL</div><div class="fav">★ FAVS</div></div>
    <div class="market-row hot"><span class="star">★</span><span class="pair">BTC/USD</span><svg viewBox="0 0 30 10"><polyline points="0,6 30,6" fill="none" stroke="#9cc9e8" stroke-width=".7"/></svg><span class="val">577.0000</span><span class="dir">▼</span></div>
    <div class="market-row"><span class="star">★</span><span class="pair">LTC/USD</span><svg viewBox="0 0 30 10"><polyline points="0,7 14,7 15,2 17,2 18,8 30,8" fill="none" stroke="#9cc9e8" stroke-width=".7"/></svg><span class="val up">15.9768</span><span class="dir up">▲</span></div>
    <div class="market-row"><span class="star">★</span><span class="pair">EUR/USD</span><svg viewBox="0 0 30 10"><polyline points="0,5 30,5" fill="none" stroke="#9cc9e8" stroke-width=".7"/></svg><span class="val">1.3808</span><span class="dir">▼</span></div>
    <div class="market-row"><span class="star">★</span><span class="pair">LTC/BTC</span><svg viewBox="0 0 30 10"><polyline points="0,3 18,3 19,8 30,8" fill="none" stroke="#9cc9e8" stroke-width=".7"/></svg><span class="val">0.0278</span><span class="dir">▼</span></div>
    <div class="market-row"><span class="star">★</span><span class="pair">BTC/EUR</span><svg viewBox="0 0 30 10"><polyline points="0,5 30,5" fill="none" stroke="#9cc9e8" stroke-width=".7"/></svg><span class="val">420.0000</span><span class="dir">▼</span></div>
    <div class="market-row"><span class="star">★</span><span class="pair">LTC/EUR</span><svg viewBox="0 0 30 10"><polyline points="0,6 30,6" fill="none" stroke="#9cc9e8" stroke-width=".7"/></svg><span class="val">11.7970</span><span class="dir">▼</span></div>
  </aside>

  <footer class="abs footer">
    <section class="abs" style="left:99px;top:18px">
      <h3><svg width="16" height="13" viewBox="0 0 16 13"><path d="M1 1.5h5.5c.8 0 1.5.7 1.5 1.5v9c0-.7-.6-1.2-1.3-1.2H1zM15 1.5H9.5C8.7 1.5 8 2.2 8 3v9c0-.7.6-1.2 1.3-1.2H15z" fill="none" stroke="#fff" stroke-width="1.2"/><path d="M2.5 4h3.5M2.5 6h3.5M2.5 8h3.5M10 4h3.5M10 6h3.5M10 8h3.5" stroke="#fff" stroke-width=".7"/></svg>Latest News</h3>
      <div class="news-item" style="margin-top:12px">
        <div class="news-date">6th March, 2014</div>
        <div class="news-title">Statement regarding recent third party audit report</div>
        <div class="news-body">On November 22nd and 23rd, 2013 an on site due diligence was carried out in respect of Korvelin Ltd.</div>
      </div>
      <div class="news-item">
        <div class="news-date">6th March, 2014</div>
        <div class="news-title">Statement regarding recent third party audit report</div>
        <div class="news-body">On November 22nd and 23rd, 2013 an on site due diligence was carried out in respect of Korvelin Ltd.</div>
      </div>
    </section>
    <span class="abs view-all">View all »</span>

    <section class="abs" style="left:278px;top:18px">
      <h3><svg width="13" height="13" viewBox="0 0 13 13"><rect x=".5" y=".5" width="12" height="12" rx="2" fill="#fff"/><path d="M4 9V7a2 2 0 0 1 2-2h4M8 3l2 2-2 2" fill="none" stroke="#353535" stroke-width="1.3"/></svg>Contact Us</h3>
      <div class="contact-line" style="margin-top:13px"><svg width="9" height="9" viewBox="0 0 10 10"><path d="M5 1L.5 5H2v4h2.3V6.5h1.4V9H8V5h1.5z" fill="#fff"/></svg><span>Harwick House, 12 Tamsin Row<br>London, E9 4QX United Kingdom</span></div>
      <div class="contact-line"><svg width="9" height="9" viewBox="0 0 10 10"><path d="M2 1c.6-.4 1.2 0 1.4.6l.4 1c.1.4 0 .7-.3.9l-.4.4c.4.9 1.1 1.6 2 2l.4-.4c.2-.3.5-.4.9-.3l1 .4c.6.2.9.8.5 1.4-.5.8-1.3 1-2.3.6C3.6 6.8 2.2 5.4 1.4 3.4 1 2.4 1.2 1.5 2 1z" fill="#fff"/></svg><span>Houston: 245 56 56 56</span></div>
      <div class="contact-line"><svg width="9" height="7" viewBox="0 0 10 7"><rect width="10" height="7" fill="#fff"/><path d="M0 0l5 4 5-4" fill="none" stroke="#353535" stroke-width=".8"/></svg><span>info@vth.co.uk</span></div>
      <div class="social" aria-label="Social links">
        <span aria-label="Social link one"></span><span aria-label="Social link two"></span><span aria-label="Social link three"></span><span aria-label="Social link four"></span>
      </div>
    </section>

    <section class="abs" style="left:437px;top:18px;width:160px;height:140px">
      <h3><svg width="15" height="11" viewBox="0 0 15 11"><rect x=".5" y=".5" width="14" height="10" rx="1" fill="#fff"/><path d="M2.5 3h10M2.5 5.5h10M2.5 8h6" stroke="#353535" stroke-width=".9"/></svg>Subscribe Newsletter</h3>
      <p class="subscribe-copy">Enter your email address to receive all news from our awesome website</p>
      <div class="subscribe-input">enter email address</div>
    </section>
    <div class="abs subscribe-btn">Submit</div>
  </footer>

</div>
</body>
</html>
```